Poster Design

Hello,

My name is Rowan Pickett and I run a vidora channel called 'CrumbleDiary'. I want a poster made for those who watch my video to purchase and put on their wall at home. The poster will be all text and as you can see, I've attached a few examples of posters which I would like it to be similar to. I use a lot of the colour #ab6f7f so it would be good to incorporate this in somewhere (maybe the background colour).
I would like the poster to say:
"Do More Of What Makes YOU Happy"
I need this poster to be for sale ready for christmas, so Im going to need the designs created as soon as possible. Im sorry for the rush.
Have fun with it and feel free to upload multiple versions of a design as well as a few designs if you like.
I look forward to seeing what you come up with.
Rowan
(Of course I will need to own all rights once the payment has been made)

```html
<!DOCTYPE html>
<html lang="en">
<head>
<meta charset="utf-8">
<title>Do More Of What Makes You Happy — Poster</title>
<link rel="stylesheet" href="https://fonts.googleapis.com/css2?family=Oswald:wght@500&family=Stint+Ultra+Condensed&family=Playfair+Display:ital@1&family=Great+Vibes&display=swap">
<style>
  :root {
    --page: #ffffff;
    --page-edge: #000000;
    --poster-red: #c40033;
    --letter: #ffffff;
    --letter-shade: #8c7f7c;
    --letter-edge: #4a1f24;
    --rule: #f3dde2;
  }
  html, body {
    margin: 0;
    padding: 0;
    width: 999px;
    height: 1200px;
    overflow: hidden;
    background: var(--page);
  }
  .page {
    position: relative;
    width: 999px;
    height: 1200px;
    box-sizing: border-box;
    border-top: 1px solid var(--page-edge);
    border-right: 1px solid var(--page-edge);
    border-bottom: 1px solid var(--page-edge);
  }
  .poster {
    position: absolute;
    left: 0;
    top: 0;
    display: block;
  }
  .poster-field { fill: var(--poster-red); }
  .headline {
    fill: var(--letter);
    filter: url(#embossed);
  }
  .headline--sans {
    font-family: "Oswald", "Arial Narrow", sans-serif;
    font-weight: 500;
  }
  .headline--slab {
    font-family: "Stint Ultra Condensed", "Rockwell", serif;
  }
  .connector--italic {
    font-family: "Playfair Display", "Georgia", serif;
    font-style: italic;
  }
  .connector--script {
    font-family: "Great Vibes", "Brush Script MT", cursive;
  }
  .rule { stroke: var(--rule); stroke-width: 1.4; }
</style>
</head>
<body>
<main class="page">
  <svg class="poster" width="999" height="1200" viewBox="0 0 999 1200" aria-label="Do more of what makes you happy">
    <defs>
      <filter id="embossed" x="-5%" y="-5%" width="115%" height="115%">
        <feMorphology in="SourceAlpha" operator="dilate" radius="1" result="thick"/>
        <feOffset in="thick" dx="1.5" dy="1.5" result="edgeShift"/>
        <feFlood flood-color="#4a1f24"/>
        <feComposite in2="edgeShift" operator="in" result="edge"/>
        <feOffset in="SourceAlpha" dx="2.5" dy="2.5" result="shadeShift"/>
        <feFlood flood-color="#8c7f7c"/>
        <feComposite in2="shadeShift" operator="in" result="shade"/>
        <feMerge>
          <feMergeNode in="edge"/>
          <feMergeNode in="shade"/>
          <feMergeNode in="SourceGraphic"/>
        </feMerge>
      </filter>
    </defs>

    <rect class="poster-field" x="78" y="38" width="792" height="1120"/>

    <text class="headline headline--sans" x="194" y="318" font-size="200" textLength="556" lengthAdjust="spacingAndGlyphs">DO MORE</text>

    <g class="divider divider--upper">
      <line class="rule" x1="230" y1="392" x2="410" y2="392"/>
      <line class="rule" x1="230" y1="396" x2="410" y2="396"/>
      <line class="rule" x1="230" y1="400" x2="410" y2="400"/>
      <line class="rule" x1="528" y1="392" x2="708" y2="392"/>
      <line class="rule" x1="528" y1="396" x2="708" y2="396"/>
      <line class="rule" x1="528" y1="400" x2="708" y2="400"/>
    </g>
    <text class="headline connector--italic" x="468" y="415" font-size="80" text-anchor="middle">Of</text>

    <text class="headline headline--slab" x="200" y="598" font-size="172" textLength="545" lengthAdjust="spacingAndGlyphs">WHAT MAKES</text>

    <g class="divider divider--lower">
      <line class="rule" x1="232" y1="709" x2="368" y2="709"/>
      <line class="rule" x1="232" y1="713" x2="368" y2="713"/>
      <line class="rule" x1="232" y1="717" x2="368" y2="717"/>
      <line class="rule" x1="572" y1="709" x2="708" y2="709"/>
      <line class="rule" x1="572" y1="713" x2="708" y2="713"/>
      <line class="rule" x1="572" y1="717" x2="708" y2="717"/>
    </g>
    <text class="headline connector--script" x="472" y="728" font-size="86" text-anchor="middle">You</text>

    <text class="headline headline--sans" x="222" y="1013" font-size="250" textLength="513" lengthAdjust="spacingAndGlyphs">HAPPY</text>
  </svg>
</main>
</body>
</html>
```